BRIGHTDESK COWORKING Website design and coding

BRIGHTDESK COWORKING

BRIGHTDESK is Galveston’s first (and currently only) shared business co-working space. We share the same upscale, casual work environment, but we work independently on our own (or our team’s) projects and goals. For only a flat $195 membership fee per month, you have your very own all-inclusive, fun, personal business office environment. Website is written (Word file #12, below); and all pictures etc provided. Galveston is a beachy, coastal, historic city an hour from Houston, Texas USA. Logo (file 11 below) is temporary only.

Target Market(s)

Outside sales people, medical students looking for study hall, Houston companies looking for local office, real estate agents, graphic artists, entrepreneurs, etc

Contact Information for Business Card

will discuss --want to combine with current business card with multiple businesses

Logo Text

BRIGHTDESK COWORKING

Coding

Coded - Design and coding required

Number of Pages Required

5+ page

Colors
ec1f27
fbed22

Requirements
Nice to have
• maroon/wine dominant with yellow and red accents, gray base are the colors of the space--website could coordinate--but open to creative ideas/combinations

```html
<!DOCTYPE html>
<html lang="en">
<head>
<meta charset="utf-8">
<title>BRIGHTDESK COWORKING</title>
<link rel="stylesheet" href="https://fonts.googleapis.com/css2?family=Playfair+Display:wght@400;700;900&family=Poppins:wght@300;400;500;600;700&display=swap">
<style>
:root{
  --maroon:#8c0a0a;
  --red:#c4161c;
  --yellow:#fbed22;
  --dark:#23242b;
  --ink:#111;
  --text:#555;
  --gray:#f1f1f1;
  --line:#d8d8d8;
}
*{margin:0;padding:0;box-sizing:border-box}
html,body{width:1200px;height:4926px;overflow:hidden}
body{position:relative;background:#fff;font-family:'Poppins',sans-serif;color:var(--text)}
.abs{position:absolute}
.serif{font-family:'Playfair Display',serif}
.photo{position:absolute}
.stripes{position:absolute;background:linear-gradient(135deg,rgba(251,237,34,.45),rgba(251,237,34,0) 75%)}
.stripes.grey{background:linear-gradient(135deg,rgba(0,0,0,.06),rgba(0,0,0,0) 75%)}

/* header */
.site-header{position:absolute;left:0;top:0;width:1200px;height:88px}
.brand{position:absolute;left:90px;top:20px;font-weight:700;font-size:17px;color:var(--maroon);letter-spacing:1px;line-height:1.1}
.brand span{display:block;color:var(--ink);font-size:15px;letter-spacing:2px}
.nav{position:absolute;top:36px;left:383px;display:flex;gap:34px;font-size:12.5px;color:#222;text-transform:uppercase;font-weight:500}
.search{position:absolute;left:1112px;top:0;width:88px;height:88px;background:var(--dark)}

/* hero */
.eyebrow{left:90px;top:220px;font-size:12px;font-weight:600;color:#222;text-transform:uppercase;display:flex;align-items:center;gap:10px}
.eyebrow::before{content:"";width:70px;height:1px;background:#222}
.hero-title{left:90px;top:252px;font-family:'Playfair Display',serif;font-weight:900;font-size:60px;line-height:58px;color:var(--ink);text-transform:uppercase}
.btn{position:absolute;background:var(--maroon);color:#fff;font-size:13px;font-weight:600;text-transform:uppercase;display:flex;align-items:center;justify-content:center;letter-spacing:.5px}
.hero-arrow{left:543px;top:543px;width:84px;height:84px;background:var(--yellow)}

/* stats */
.stat{position:absolute;top:720px;display:flex;align-items:center;gap:12px}
.stat b{font-size:60px;font-weight:500;color:var(--ink);line-height:1}
.stat span{font-size:13px;font-weight:600;color:#222;text-transform:uppercase;line-height:16px}
.divider{position:absolute;top:726px;width:1px;height:56px;background:var(--line)}

/* about */
.about-bg{left:0;top:875px;width:1110px;height:570px;background:var(--gray)}
.section-title{font-family:'Playfair Display',serif;font-weight:900;color:var(--ink);font-size:44px;line-height:48px;text-transform:uppercase}
.section-sub{font-family:'Playfair Display',serif;font-weight:400;color:#222;font-size:35px;line-height:42px;text-transform:uppercase}
.body-copy{font-size:14.5px;line-height:27px;color:var(--text)}
.price{left:913px;top:1383px;width:287px;height:125px;background:var(--yellow);padding:20px 0 0 30px}
.price b{display:block;font-size:52px;font-weight:700;color:var(--ink);line-height:62px}
.price span{font-size:14.5px;font-weight:600;color:var(--ink)}

/* amenity cards */
.card{position:absolute;top:1735px;width:267px;height:283px}
.card-label{position:absolute;left:0;right:0;bottom:20px;text-align:center;font-family:'Playfair Display',serif;font-weight:700;font-size:20px;color:#fff}

/* philosophy tabs */
.tabs{left:90px;top:3652px;width:1020px;height:32px;border-bottom:1px solid var(--line);font-size:11.5px;font-weight:600;text-transform:uppercase;color:#222}
.tab{position:absolute;top:0}
.tab.active{color:var(--red);border-bottom:2px solid var(--red);padding-bottom:9px}

/* footer */
.footer{left:0;top:4437px;width:1200px;height:489px;background:var(--dark)}
.mailing{left:569px;top:4361px;width:631px;height:149px;background:var(--yellow)}
.mailing-label{position:absolute;left:62px;top:40px;font-size:11.5px;font-weight:600;color:#222;text-transform:uppercase}
.mailing-input{position:absolute;left:62px;top:67px;width:357px;height:40px;background:#fff;font-size:14px;color:#999;padding:10px 0 0 40px}
.mailing-btn{position:absolute;left:419px;top:67px;width:117px;height:40px;background:var(--maroon);color:#fff;font-size:11.5px;font-weight:700;display:flex;align-items:center;justify-content:center}
.foot-brand{left:90px;top:4588px;color:var(--maroon);font-weight:700;font-size:38px;line-height:40px;letter-spacing:1px}
.foot-brand span{display:block;color:#fff;font-size:24px;letter-spacing:3px;padding-left:22px}
.social{position:absolute;top:4685px;width:36px;height:36px;border-radius:50%;background:#3a3b43}
.foot-col{position:absolute;top:4592px;color:#ddd;font-size:12.5px;line-height:17px}
.foot-col h4{font-family:'Playfair Display',serif;font-weight:700;font-size:15px;color:#fff;text-transform:uppercase;margin-bottom:22px;letter-spacing:.5px}
.item{position:relative;padding-left:22px;margin-bottom:14px}
.item svg{position:absolute;left:0;top:2px}
.to-top{left:1088px;top:4845px;width:40px;height:40px;border-radius:50%;background:var(--red)}
.copyright{left:0;top:4888px;width:1200px;text-align:center;color:#fff;font-size:12px;font-weight:500}
</style>
</head>
<body>

<header class="site-header">
  <div class="brand">BRIGHTDESK<span>COWORKING</span></div>
  <nav class="nav"><span>About</span><span>Amenities</span><span>Membership</span><span>Pictures</span><span>The BrightDesk Philosophy</span><span>Contact</span></nav>
  <div class="search">
    <svg width="88" height="88" viewBox="0 0 88 88"><circle cx="42" cy="41" r="10" fill="none" stroke="#fff" stroke-width="2"/><line x1="49" y1="48" x2="56" y2="55" stroke="#fff" stroke-width="2"/></svg>
  </div>
</header>

<!-- hero -->
<div class="abs eyebrow">Welcome BrightDesk Coworking</div>
<h1 class="abs hero-title">Your<br>Coworking<br>Space</h1>
<div class="btn" style="left:90px;top:462px;width:141px;height:46px">Contact Us</div>
<div class="photo" role="img" aria-label="Shared kitchen with pendant lamps, bar counter and stools" style="left:543px;top:88px;width:657px;height:539px;background:linear-gradient(135deg,#b9b2a4 0%,#8a7a62 45%,#4a2b2a 80%,#3a3535 100%)"></div>
<div class="abs hero-arrow"><svg width="84" height="84" viewBox="0 0 84 84"><path d="M42 32v20M35 45l7 7 7-7" fill="none" stroke="#222" stroke-width="2"/></svg></div>

<!-- stats -->
<div class="stat" style="left:287px"><b>14</b><span>Meeting<br>Room</span></div>
<div class="divider" style="left:481px"></div>
<div class="stat" style="left:533px"><b>06</b><span>Event<br>Space</span></div>
<div class="divider" style="left:720px"></div>
<div class="stat" style="left:772px"><b>15</b><span>Creative<br>Studio</span></div>

<!-- about -->
<div class="abs about-bg"></div>
<div class="stripes grey" role="img" aria-label="Diagonal stripe pattern" style="left:0;top:875px;width:215px;height:215px"></div>
<div class="photo" role="img" aria-label="Lounge with white sofa, yellow and black office chairs and lockers" style="left:90px;top:969px;width:395px;height:476px;background:linear-gradient(160deg,#d6d3cc 0%,#a9aab0 40%,#6b6664 70%,#c9a23a 100%)"></div>
<div class="abs" style="left:585px;top:990px">
  <div class="section-title">About</div>
  <div class="section-sub">BrightDesk Coworking</div>
</div>
<p class="abs body-copy" style="left:585px;top:1100px;width:430px">BRIGHTDESK is Galveston’s first (and currently only) shared business co-working space. We share the same upscale, casual work environment, but we work independently on our own (or our team’s) projects and goals. For only a flat $195 membership fee per month, you have your very own all-inclusive, fun, personal business office environment.</p>
<svg class="abs" style="left:543px;top:1374px" width="322" height="12"><line x1="0" y1="6" x2="318" y2="6" stroke="#999"/><path d="M312 1l6 5-6 5" fill="none" stroke="#999"/></svg>
<div class="abs price"><b>$195</b><span>Membership fee per month</span></div>

<!-- amenities -->
<div class="abs" style="left:90px;top:1592px">
  <div class="section-title">Amenities</div>
  <div class="section-sub">BrightDesk Coworking</div>
</div>
<p class="abs body-copy" style="left:545px;top:1598px;width:440px">BRIGHTDESK is the first Galveston co-working space, and offers all of the following features, all included in your monthly $195 membership fee:</p>
<div class="card" role="img" aria-label="Laptop and phone on a wooden desk with wifi router" style="left:90px;background:linear-gradient(150deg,#5b3a22,#c07a35 60%,#7a4a25)"><div class="card-label">Free Wifi</div></div>
<div class="card" role="img" aria-label="Worker with headset at a desk" style="left:371px;background:linear-gradient(150deg,#2a2a2a,#555 55%,#9a9a9a)"><div class="card-label">24 hour access</div></div>
<div class="card" role="img" aria-label="Office entry with plant and kitchen counter" style="left:652px;background:linear-gradient(160deg,#4a3a2c,#8a7a66 55%,#3b5a28)"><div class="card-label" style="top:22px;bottom:auto;text-align:left;left:36px;line-height:28px">Keyless, digital<br>door entry</div>
  <div class="abs" style="left:206px;top:222px;width:61px;height:61px;background:var(--yellow)"><svg width="61" height="61" viewBox="0 0 61 61"><path d="M22 30.5h18M34 24.5l6 6-6 6" fill="none" stroke="#222" stroke-width="2"/></svg></div>
</div>
<div class="card" role="img" aria-label="Laptop and coffee cup on dark wood" style="left:934px;background:linear-gradient(150deg,#3a2618,#6a4426 55%,#2e1e14)"><div class="card-label">Mail service</div></div>
<div class="stripes grey" role="img" aria-label="Diagonal stripe pattern" style="left:0;top:1930px;width:90px;height:150px"></div>

<!-- membership -->
<h2 class="abs section-title" style="left:90px;top:2236px">Membership</h2>
<div class="abs body-copy" style="left:90px;top:2300px;width:420px;font-size:14px;line-height:21px">
  <p style="margin-bottom:21px">For only $195 a month, charged to your credit card, you get the all-inclusive amenities listed above, for one flat fee. The only “extras” are for copies, on a per-copy basis.</p>
  <p style="margin-bottom:21px">WiFi, coffee, use of the conference room, office use, use of the kitchen and all the other features listed under “AMENITIES” above, are INCLUDED at no additional cost.</p>
  <p>WiFi, coffee, use of the conference room, office use, use of the kitchen and all the other features listed under “AMENITIES” above, are INCLUDED at no additional cost.</p>
</div>
<div class="btn" style="left:90px;top:2599px;width:141px;height:42px">Read More</div>
<div class="abs" style="left:703px;top:2265px;width:497px;height:510px;background:var(--maroon)"></div>
<div class="stripes" role="img" aria-label="Diagonal stripe pattern" style="left:990px;top:2565px;width:210px;height:210px;background:linear-gradient(315deg,rgba(251,237,34,.6),rgba(251,237,34,0) 75%)"></div>
<div class="photo" role="img" aria-label="Open office with desks, black chairs, sofa and lockers" style="left:589px;top:2154px;width:504px;height:502px;background:linear-gradient(170deg,#d9d6d0 0%,#9fa3a6 40%,#4a4a4c 75%,#2a2a2c 100%)"></div>

<!-- gallery -->
<h2 class="abs section-title" style="left:0;top:2866px;width:1200px;text-align:center">Our Gallery</h2>
<div class="photo" role="img" aria-label="Kitchen counter with a plant in a pink vase" style="left:0;top:2943px;width:508px;height:481px;background:linear-gradient(160deg,#3a2a2e,#6a6462 45%,#d8a88e 80%,#a98a5e)"></div>
<div class="photo" role="img" aria-label="Lounge with black sofas and glass partition" style="left:525px;top:2943px;width:337px;height:481px;background:linear-gradient(170deg,#c9b78a,#8a7c62 45%,#2a2a2a)"></div>
<div class="photo" role="img" aria-label="Conference table with pendant lamps" style="left:879px;top:2943px;width:321px;height:231px;background:linear-gradient(160deg,#e0dcd2,#c9a14e 55%,#6a5232)"></div>
<div class="photo" role="img" aria-label="Meeting room with long table and stools" style="left:879px;top:3193px;width:321px;height:231px;background:linear-gradient(160deg,#e3e0da,#c09248 55%,#3e2e22)"></div>
<div class="stripes" role="img" aria-label="Diagonal stripe pattern" style="left:0;top:3424px;width:210px;height:100px"></div>

<!-- philosophy -->
<h2 class="abs section-title" style="left:0;top:3524px;width:1200px;text-align:center;line-height:54px">The BrightDesk<br>Philosophy</h2>
<div class="abs tabs">
  <span class="tab active" style="left:0">Work outside the home</span>
  <span class="tab" style="left:229px">Work it out with your coworkers</span>
  <span class="tab" style="left:531px">BrightDesk the competition</span>
  <span class="tab" style="left:766px">Work out the path to your success</span>
</div>
<div class="photo" role="img" aria-label="Lounge with black leather sofas, lockers and a plant" style="left:90px;top:3753px;width:531px;height:465px;background:linear-gradient(160deg,#c9ccd0,#8a8e92 35%,#6a2a30 60%,#2a2a2a 100%)"></div>
<div class="stripes" role="img" aria-label="Diagonal stripe pattern" style="left:0;top:4128px;width:170px;height:172px"></div>
<h3 class="abs serif" style="left:676px;top:3852px;font-size:27px;font-weight:700;color:var(--ink);text-transform:uppercase">Work outside the home</h3>
<p class="abs body-copy" style="left:676px;top:3894px;width:440px;font-size:14px;line-height:25px">Free yourself for the burdens of house or school, and work in an environment that MOTIVATES you instead of DISTRACTS you. Meet like-minded people that can help you along, and yet you have the option to work in a quiet-and very comfortable – private office cubicle. Perfect for medical students, entrepreneurs, designers, writers, business reps away from headquarters, contractors working on bids or plans, or anyone needing a flexible, fun business environment!</p>

<!-- footer -->
<footer>
  <div class="abs footer"></div>
  <div class="abs mailing">
    <div class="mailing-label">Join our mailing list</div>
    <div class="mailing-input"><svg style="position:absolute;left:14px;top:14px" width="16" height="12"><rect x=".5" y=".5" width="15" height="11" fill="#aaa"/><path d="M1 1l7 5 7-5" fill="none" stroke="#fff"/></svg>Enter your email address</div>
    <div class="mailing-btn">SUBSCRIBE</div>
  </div>
  <div class="abs foot-brand">BRIGHTDESK<span>COWORKING</span></div>
  <div class="social" style="left:141px" aria-label="Social link"></div>
  <div class="social" style="left:186px" aria-label="Social link"></div>
  <div class="social" style="left:232px" aria-label="Social link"></div>

  <div class="foot-col" style="left:376px;width:240px">
    <h4>Contact Us</h4>
    <div class="item"><svg width="12" height="10"><rect width="12" height="10" fill="#fbed22"/><path d="M0 0l6 5 6-5" fill="none" stroke="#23242b"/></svg>Email:<br>hello@brightdeskcowork.com</div>
    <div class="item"><svg width="12" height="12" viewBox="0 0 12 12"><path d="M2 1l3 0 1 3-2 1c1 2 2 3 3 3l1-2 3 1v3c-6 0-10-4-10-10z" fill="#fbed22"/></svg>Phone:<br>888-555-0142</div>
  </div>
  <div class="foot-col" style="left:648px;width:210px">
    <h4>Physical Location</h4>
    <div class="item"><svg width="11" height="14" viewBox="0 0 11 14"><path d="M5.5 0a5.5 5.5 0 0 0-5.5 5.5c0 4 5.5 8.5 5.5 8.5s5.5-4.5 5.5-8.5A5.5 5.5 0 0 0 5.5 0z" fill="#fbed22"/><circle cx="5.5" cy="5.5" r="2" fill="#23242b"/></svg>BrightDesk Coworking<br>418 Harbor Ave, Suite 101<br>Galveston, TX 77550</div>
  </div>
  <div class="foot-col" style="left:873px;width:230px">
    <h4>Owner</h4>
    <div style="margin-bottom:16px">Halvorsen Holdings</div>
    <div class="item"><svg width="12" height="10"><rect width="12" height="10" fill="#fbed22"/><path d="M0 0l6 5 6-5" fill="none" stroke="#23242b"/></svg>Email:<br>owner@halvorsenholdings.com</div>
    <div class="item"><svg width="12" height="12" viewBox="0 0 12 12"><path d="M2 1l3 0 1 3-2 1c1 2 2 3 3 3l1-2 3 1v3c-6 0-10-4-10-10z" fill="#fbed22"/></svg>Phone:<br>713-555-0198</div>
    <div class="item"><svg width="11" height="14" viewBox="0 0 11 14"><path d="M5.5 0a5.5 5.5 0 0 0-5.5 5.5c0 4 5.5 8.5 5.5 8.5s5.5-4.5 5.5-8.5A5.5 5.5 0 0 0 5.5 0z" fill="#fbed22"/><circle cx="5.5" cy="5.5" r="2" fill="#23242b"/></svg>Halvorsen Holdings<br>120 Bayou Way, Suite 200<br>Houston, TX 77002</div>
  </div>
  <div class="abs to-top"><svg width="40" height="40" viewBox="0 0 40 40"><path d="M20 26V14M15 19l5-5 5 5" fill="none" stroke="#fff" stroke-width="1.5"/></svg></div>
  <div class="abs copyright">COPYRIGHT © 2020, BRIGHTDESK COWORKING. ALL RIGHTS RESERVED</div>
</footer>

</body>
</html>
```